AUSTRALIA SUPPLEMENT - Protein label design - CREATIVE, FEMININE, UNIQUE

I need help with the design of what will be my line of supplements. (Protein, plant base, collagen , BCAAs, etc)
I'm starting off with protein isolate - with the flavours VANILLA, CHOCOLATE, BOYSENBERRY, HONEYCOMB.
I need help with the design of what the product will look like for my range.
(Great opportunity for further work)

Looking for a unique, elegant, stand out, feminine design, some slight sparkle or something that stands out on a shelf.
With symbols to represent what's in it, raised text. with some quirky cute things on it. (not sure what) Something that captured young womens eyes and easy to understand. things on it that appeals to women such as
LOW CALORIE, GREAT TASTING, GLUTEN FREE, 100 NATURAL, NATURALLY SWEETENED, HIGH PROTEIN.etc and whatever you can think of (open to ideas) but within KMO guidelines.

Mostly just after the look and creativity of what the front will look like. Don't have to worry about the back area.

My market will be for females aged 18-35

I have a activewear line called DORUMEN which will go with this. which I will attach the logo below amongst some other things that match my packaging. (again open to ideas)

I have attached a label of what one will look like( EXAMPLE).
. Among others that look nice But again I want to be different, unique to stand out. I don't want it to look like these. it's just the only ones I found online I liked that suit my market.

Feel free to ask any questions! :)
Updates

Extending time as I want this to be to be what will be on the shelves of many stores. I know that needs time to be able to do a quality job.

Target Market(s)

18-35

Industry/Entity Type

Supplement

Font styles to use
Serif
Script

Colors
f9d9e8
ffffff
fbd3d4
ecf7fb
e4daeb
cfeae6
eea4c8
fdfad7
f59195

Requirements
Must have
• Word - DORUMEN
PROTEIN ISOLATE
FLAVOUR
SYMBOLS

Looking for a unique, elegant, stand out, colour, feminine design, some slight sparkle or something that stands out on a shelf.

IT WILL BE ON A WHITE TUB or CLEAR - Perhaps detail on the lid
Nice to have
• Looking for a unique, elegant, stand out, colour, feminine design, some slight sparkle or something that stands out on a shelf. Something artsy.

will be on a white or clear tub with a white label background (possibly)
Should not have
• I don’t want it dark looking.
Something bright, vibrant, whites, pinks, sparkles (maybe) colours.

I don't want the word activewear on it.

```html
<!DOCTYPE html>
<html lang="en">
<head>
<meta charset="utf-8">
<title>DORUMEN Protein Isolate Label</title>
<link rel="stylesheet" href="https://fonts.googleapis.com/css2?family=Roboto:wght@500;700;900&family=Tinos&display=swap">
<style>
  :root {
    --canvas: #ffffff;
    --label-top: #f4f4f5;
    --label-mid: #ffffff;
    --ink: #2a2a2c;
    --accent-red: #d81e45;
    --band-dark: #c1143a;
    --band-light: #e12a4f;
    --crack-light: #f7d3dc;
    --crack-deep: #eea1b3;
    --white: #ffffff;
  }
  * { box-sizing: border-box; margin: 0; padding: 0; }
  html, body {
    width: 1200px;
    height: 1200px;
    overflow: hidden;
    background: var(--canvas);
  }
  .canvas {
    position: relative;
    width: 1200px;
    height: 1200px;
  }
  .label {
    position: absolute;
    left: 100px;
    top: 240px;
    width: 1000px;
    height: 720px;
    overflow: hidden;
    background: linear-gradient(180deg, var(--label-top) 0%, var(--label-mid) 40%);
  }
  .label__pattern {
    position: absolute;
    left: 0;
    top: 250px;
    width: 100%;
    height: 470px;
    background: linear-gradient(180deg, rgba(247, 211, 220, 0) 0%, var(--crack-light) 30%, var(--crack-deep) 100%);
  }
  .brand {
    position: absolute;
    top: 124px;
    width: 100%;
    text-align: center;
    font-family: "Roboto", sans-serif;
    font-weight: 500;
    font-size: 44px;
    line-height: 1;
    letter-spacing: 1px;
    color: var(--ink);
  }
  .product-type {
    position: absolute;
    top: 196px;
    width: 100%;
    text-align: center;
    font-family: "Roboto", sans-serif;
    font-weight: 900;
    font-size: 112px;
    line-height: 1;
    color: var(--ink);
  }
  .product-sub {
    position: absolute;
    top: 318px;
    width: 100%;
    text-align: center;
    font-family: "Roboto", sans-serif;
    font-weight: 500;
    font-size: 34px;
    color: var(--accent-red);
  }
  .claims-band {
    position: absolute;
    top: 378px;
    left: 0;
    width: 100%;
    height: 120px;
    background: linear-gradient(90deg, var(--band-dark), var(--band-light) 50%, var(--band-dark));
    display: flex;
    justify-content: center;
    align-items: center;
    gap: 40px;
  }
  .claims-band svg { display: block; }
  .flavour-tag {
    position: absolute;
    top: 558px;
    left: 50%;
    transform: translateX(-50%);
    width: 270px;
    height: 118px;
    border-radius: 50%;
    background: var(--white);
    border: 5px solid var(--accent-red);
    text-align: center;
    padding-top: 10px;
  }
  .flavour-tag__name {
    font-family: "Tinos", serif;
    font-size: 50px;
    line-height: 1.05;
    color: var(--ink);
  }
  .flavour-tag__count {
    font-family: "Roboto", sans-serif;
    font-weight: 700;
    font-size: 24px;
    color: var(--ink);
  }
</style>
</head>
<body>
<main class="canvas">
  <section class="label">
    <div class="label__pattern" role="img" aria-label="Soft pink cracked marble texture"></div>
    <div class="brand">DORUMEN</div>
    <h1 class="product-type">SUPPLEMENT</h1>
    <p class="product-sub">PROTEIN ISOLATE</p>
    <div class="claims-band">
      <svg width="90" height="80" viewBox="0 0 90 80" aria-label="Claim badge"><rect x="5" y="10" width="80" height="60" rx="8" fill="none" stroke="#fff" stroke-width="4"/></svg>
      <svg width="80" height="80" viewBox="0 0 80 80" aria-label="Claim badge"><circle cx="40" cy="40" r="34" fill="none" stroke="#fff" stroke-width="4"/></svg>
      <svg width="80" height="80" viewBox="0 0 80 80" aria-label="Claim badge"><circle cx="40" cy="40" r="34" fill="none" stroke="#fff" stroke-width="4"/></svg>
      <svg width="90" height="80" viewBox="0 0 90 80" aria-label="Claim badge"><rect x="5" y="10" width="80" height="60" fill="none" stroke="#fff" stroke-width="4"/></svg>
    </div>
    <div class="flavour-tag">
      <div class="flavour-tag__name">Vanila</div>
      <div class="flavour-tag__count">120 Tablets</div>
    </div>
  </section>
</main>
</body>
</html>
```